Corporate Design für QUR Beratung / Entwicklung
Zielgruppe
Freiberufler. QUR Beratung / Entwicklung .
Aufgabenstellung
Slogan:
Your Dedicated Workflow Logic & Operations Automation Partner ( DWLOP )

```html
<!DOCTYPE html>
<html lang="en">
<head>
<meta charset="utf-8">
<title>DWLOP – Corporate Design</title>
<link href="https://fonts.googleapis.com/css2?family=Oswald:wght@400;500&family=Open+Sans:wght@400;600;700&display=swap" rel="stylesheet">
<style>
:root{
  --navy:#2e3a6e;
  --navy-dark:#26305c;
  --grey:#9a9a9c;
  --grey-mid:#b9b9bb;
  --grey-text:#6d6d70;
  --paper:#ffffff;
  --board:#f3f3f4;
  --ink:#333;
}
*{margin:0;padding:0;box-sizing:border-box}
html,body{width:1200px;height:633px;overflow:hidden;background:var(--board)}
body{position:relative;font-family:"Open Sans",Arial,sans-serif;color:var(--ink)}
.band{position:absolute;left:0;width:1200px}
.band--top{top:0;height:286px;background:#f6f6f7}
.band--navy{top:286px;height:216px;background:var(--navy)}
.band--bottom{top:502px;height:131px;background:#fafafa}
.tile--grey{position:absolute;left:0;top:502px;width:155px;height:109px;background:var(--grey)}

/* brand lockup */
.brand{position:absolute;display:flex;align-items:flex-start;gap:.45em}
.brand__square{width:1.6em;height:1.6em;background:var(--navy);flex:none;margin-top:.1em}
.brand__text{display:flex;flex-direction:column}
.brand__name{font-family:"Oswald","Arial Narrow",sans-serif;font-weight:500;font-size:1.6em;line-height:1;letter-spacing:.04em;color:var(--navy)}
.brand__claim{font-family:"Oswald","Arial Narrow",sans-serif;font-weight:400;font-size:.62em;line-height:1.25;color:var(--grey-text);text-transform:uppercase;margin-top:.35em;letter-spacing:.02em;white-space:nowrap}
.brand__owner{font-family:"Oswald","Arial Narrow",sans-serif;font-size:.55em;color:var(--grey-text);text-transform:uppercase;margin-top:.25em;white-space:nowrap}
.brand--light .brand__square{background:#c6c6c8}
.brand--light .brand__name{color:#e4e4e6}
.brand--light .brand__claim,.brand--light .brand__owner{color:#d0d0d3}
.brand--white .brand__square{background:#fff}
.brand--white .brand__name,.brand--white .brand__claim,.brand--white .brand__owner{color:#fff}
.brand--mutedgrey .brand__square{background:#c9c9cb}
.brand--mutedgrey .brand__name{color:#b8b8ba}
.brand--mutedgrey .brand__claim,.brand--mutedgrey .brand__owner{color:#c2c2c4}

.sheet{position:absolute;background:var(--paper);box-shadow:0 2px 8px rgba(0,0,0,.18)}
.letter{left:310px;top:41px;width:387px;height:548px}
.letter__sender{position:absolute;left:44px;top:146px;font-size:5.6px;color:var(--navy);border-bottom:.5px solid #bbb;width:300px;padding-bottom:2px}
.letter__body{position:absolute;left:44px;top:166px;width:300px;font-size:4.6px;line-height:6.4px;color:#444;text-align:justify}
.letter__body p{margin-bottom:6px}
.letter__watermark{position:absolute;left:86px;top:300px;font-size:30px;opacity:.14}
.letter__signature{position:absolute;left:238px;top:360px;width:90px;height:48px;background:linear-gradient(120deg,rgba(46,58,110,.12),rgba(46,58,110,.04))}
.letter__footer{position:absolute;left:0;bottom:0;width:100%;height:60px;border-top:1px solid #999;display:flex;gap:24px;padding:8px 44px;font-size:4.4px;line-height:6px;color:#555}
.letter__footer strong{color:var(--navy)}

.card{width:205px;height:125px}
.card--navy{left:730px;top:43px;background:var(--navy)}
.card--white{left:962px;top:43px}
.card__person{position:absolute;left:124px;top:32px;font-size:7.5px;font-weight:700;color:var(--ink)}
.card__role{font-weight:400;font-size:5.5px;display:block;color:#555}
.card__contacts{position:absolute;left:114px;top:52px;list-style:none;font-size:4.6px;line-height:10px;color:#555}
.card__contacts li{display:flex;align-items:center;gap:4px}
.card__contacts svg{width:5px;height:5px;fill:var(--navy)}

.envelope{left:730px;top:184px;width:437px;height:399px}
.envelope__window{position:absolute;left:25px;top:96px;width:175px;height:64px;border-radius:12px;background:#fbfbfb;box-shadow:inset 0 0 3px rgba(0,0,0,.15)}
.envelope__flap{position:absolute;left:0;top:209px;width:437px;height:120px}
</style>
</head>
<body>
<div class="band band--top"></div>
<div class="band band--navy"></div>
<div class="band band--bottom"></div>
<div class="tile--grey"></div>

<div class="brand" style="left:59px;top:112px;font-size:24px">
  <span class="brand__square"></span>
  <span class="brand__text"><span class="brand__name">DWLOP</span><span class="brand__claim">Workflow Logic &amp; Operations<br>Automation Partner</span><span class="brand__owner">Dipl.-Ing. (FH) Lena Hartwig</span></span>
</div>
<div class="brand brand--light" style="left:59px;top:335px;font-size:24px">
  <span class="brand__square"></span>
  <span class="brand__text"><span class="brand__name">DWLOP</span><span class="brand__claim">Workflow Logic &amp; Operations<br>Automation Partner</span><span class="brand__owner">Dipl.-Ing. (FH) Lena Hartwig</span></span>
</div>
<div class="brand brand--white" style="left:26px;top:530px;font-size:9px">
  <span class="brand__square"></span>
  <span class="brand__text"><span class="brand__name">DWLOP</span><span class="brand__claim">Workflow Logic &amp; Operations<br>Automation Partner</span><span class="brand__owner">Dipl.-Ing. (FH) Lena Hartwig</span></span>
</div>
<div class="brand brand--mutedgrey" style="left:178px;top:530px;font-size:9px">
  <span class="brand__square"></span>
  <span class="brand__text"><span class="brand__name">DWLOP</span><span class="brand__claim">Workflow Logic &amp; Operations<br>Automation Partner</span><span class="brand__owner">Dipl.-Ing. (FH) Lena Hartwig</span></span>
</div>

<section class="sheet letter">
  <div class="brand" style="left:44px;top:27px;font-size:10px">
    <span class="brand__square"></span>
    <span class="brand__text"><span class="brand__name">DWLOP</span><span class="brand__claim">Workflow Logic &amp; Operations<br>Automation Partner</span><span class="brand__owner">Dipl.-Ing. (FH) Lena Hartwig</span></span>
  </div>
  <div class="letter__sender">Your Company · Your adress 12 · 34567 Your town</div>
  <div class="letter__body">
    <p>Lorem ipsum dolor sit amet, consectetur adipiscing elit. Maecenas porttitor augue justo, sit amet egestas sapien luctus ultrices. Donec arcu dolor, tincidunt sit amet mi id, laoreet pretium enim. Sed fermentum, dui vel hendrerit sodales, lectus nibh molestie tortor, id fermentum velit urna a diam. Aenean efficitur turpis eu lorem porttitor, et tincidunt leo aliquam. Fusce vel facilisis massa, euismod ullamcorper neque. Suspendisse sodales et nisl ut eleifend. Aliquam nec varius diam. Donec quis enim dictum, tempus nunc et, auctor quam. Suspendisse potenti. Quisque accumsan egestas metus. Morbi faucibus, libero at rhoncus feugiat, dui tellus aliquet purus, a porta leo sem et nunc. Maecenas pretium sit amet mi id vulputate.</p>
    <p>Phasellus id ante id ipsum cursus luctus. Praesent purus elit, ornare sit amet ultricies ac, dignissim a eros. Phasellus vestibulum odio et ipsum mattis maximus. Vivamus suscipit pulvinar tellus eu congue. Aenean quis dui varius, ullamcorper arcu sit amet, vehicula odio. Nunc dui tellus, blandit lacinia sapien eget, venenatis porttitor ex. Sed molestie viverra elit, sit amet condimentum mi finibus et.</p>
    <p>Lorem ipsum dolor sit amet, consectetur adipiscing elit. Maecenas porttitor augue justo, sit amet egestas sapien luctus ultrices. Donec arcu dolor, tincidunt sit amet mi id, laoreet pretium enim. Sed fermentum, dui vel hendrerit sodales, lectus nibh molestie tortor, id fermentum velit urna a diam. Aenean efficitur turpis eu lorem porttitor, et tincidunt leo aliquam. Fusce vel facilisis massa, euismod ullamcorper neque. Suspendisse sodales et nisl ut eleifend. Morbi faucibus, libero at rhoncus feugiat, dui tellus aliquet purus.</p>
    <p>Phasellus id ante id ipsum cursus luctus. Praesent purus elit, ornare sit amet ultricies ac, dignissim a eros. Vivamus suscipit pulvinar tellus eu congue. Nunc dui tellus, blandit lacinia sapien eget, venenatis porttitor ex. Cras vel enim, congue at purus vitae, tempor lacinia dolor.</p>
  </div>
  <div class="brand brand--mutedgrey letter__watermark"><span class="brand__square"></span><span class="brand__text"><span class="brand__name">DWLOP</span></span></div>
  <div class="letter__signature" role="img" aria-label="Handwritten signature"></div>
  <footer class="letter__footer">
    <div><strong>Your Company</strong><br>CEO Your Name<br>Your adress 12<br>34567 Your Town</div>
    <div>☎ 1234 – 56 78 90 00<br>✆ 1234 – 56 78 90 10<br>✉ your.name@yourweb.de<br>⌂ www.yourweb.de</div>
    <div>Bank details:<br>IBAN: DE00 0000 0000 0000 0000 00<br>BIC: XXXXDEXX<br>VAT ID: DE 000000000</div>
  </footer>
</section>

<section class="sheet card card--navy">
  <div class="brand brand--white" style="left:22px;top:26px;font-size:13px">
    <span class="brand__square"></span>
    <span class="brand__text"><span class="brand__name">DWLOP</span><span class="brand__claim">Workflow Logic &amp; Operations<br>Automation Partner</span><span class="brand__owner">Dipl.-Ing. (FH) Lena Hartwig</span></span>
  </div>
</section>
<section class="sheet card card--white">
  <div class="brand" style="left:14px;top:32px;font-size:8px">
    <span class="brand__square"></span>
    <span class="brand__text"><span class="brand__name">DWLOP</span><span class="brand__claim">Workflow Logic &amp; Operations<br>Automation Partner</span><span class="brand__owner">Dipl.-Ing. (FH) Lena Hartwig</span></span>
  </div>
  <div class="card__person">Your Name<span class="card__role">CEO</span></div>
  <ul class="card__contacts">
    <li><svg viewBox="0 0 10 10"><path d="M5 0a3.5 3.5 0 0 0-3.5 3.5C1.5 6 5 10 5 10s3.5-4 3.5-6.5A3.5 3.5 0 0 0 5 0z"/></svg>Your Adress 12, 34567 Your Town</li>
    <li><svg viewBox="0 0 10 10"><rect x="2" y="0" width="6" height="10" rx="1"/></svg>+00 123 456 789</li>
    <li><svg viewBox="0 0 10 10"><rect x="0" y="2" width="10" height="7" rx="1"/></svg>+00 123 456 789</li>
    <li><svg viewBox="0 0 10 10"><path d="M0 2h10v6H0z"/></svg>yourname@your-web.de</li>
    <li><svg viewBox="0 0 10 10"><circle cx="5" cy="5" r="5"/></svg>www.your-web.de</li>
  </ul>
</section>

<section class="sheet envelope">
  <div class="brand" style="left:24px;top:26px;font-size:10px">
    <span class="brand__square"></span>
    <span class="brand__text"><span class="brand__name">DWLOP</span><span class="brand__claim">Workflow Logic &amp; Operations<br>Automation Partner</span><span class="brand__owner">Dipl.-Ing. (FH) Lena Hartwig</span></span>
  </div>
  <div class="envelope__window"></div>
  <svg class="envelope__flap" viewBox="0 0 437 120" preserveAspectRatio="none">
    <polygon points="0,0 437,0 437,40 0,40" fill="#2e3a6e"/>
    <polygon points="0,0 437,0 437,10 218,90 0,10" fill="#2e3a6e"/>
    <polygon points="0,22 218,100 437,22 437,28 218,108 0,28" fill="#ececee"/>
    <polygon points="0,28 218,108 437,28 437,120 0,120" fill="#ffffff"/>
  </svg>
  <div class="brand" style="left:18px;top:330px;font-size:9px">
    <span class="brand__square"></span>
    <span class="brand__text"><span class="brand__name">DWLOP</span><span class="brand__claim">Workflow Logic &amp; Operations<br>Automation Partner</span><span class="brand__owner">Dipl.-Ing. (FH) Lena Hartwig</span></span>
  </div>
</section>
</body>
</html>
```